Binder design for a veterinary clinic

We are seeking a talented designer to create a standout design for ring binders specifically for our veterinary clinic. These binders will be used to organize materials from our Continuing Professional Development (CPD) projects for colleagues and interns. The design should be clean, professional, and align with our brand guidelines. To give you a better understanding of our branding, we’ve included the design of our vehicles as a reference. As additional reference, please visit www.tierpraxoland.at

Target Market(s)

veterinarians

Industry/Entity Type

Veterinary

Font styles to use
Sans Serif

Colors
0054AA
0677BA
7BADD7
CADEEF
E8F1F8
FFC000
F8CF3A
FAE287
FDF2CF
FEFAEE

Requirements
Must have
• Our Logo an a clean design
Should not have
• to much images

```html
<!DOCTYPE html>
<html lang="de">
<head>
<meta charset="utf-8">
<title>Tierpraxoland – Ordner</title>
<link href="https://fonts.googleapis.com/css2?family=Montserrat:wght@600;700;800&family=Open+Sans:wght@400;600&display=swap" rel="stylesheet">
<style>
  :root {
    --navy: #253749;
    --navy-deep: #1f2f3f;
    --navy-ring: #213243;
    --gold: #cd9a2c;
    --white: #ffffff;
    --paper: #ffffff;
    --trim: #4caf50;
    --measure: #7a8088;
    --measure-text: #1c2530;
    --hole: #b0141c;
    --label-grey: #a7a8aa;
    --text-dark: #26364a;
    --text-soft: #6b7480;
  }
  html, body {
    margin: 0;
    padding: 0;
    width: 1200px;
    height: 637px;
    overflow: hidden;
    background: var(--white);
  }
  .binder {
    display: block;
    width: 1200px;
    height: 637px;
  }
  .brand-name { font-family: "Montserrat", sans-serif; font-weight: 800; }
  .brand-tag { font-family: "Montserrat", sans-serif; font-weight: 700; }
  .contact { font-family: "Open Sans", sans-serif; font-size: 9px; }
  .contact .strong { fill: var(--text-dark); }
  .contact .soft { fill: var(--text-soft); }
  .measure-label { font-family: "Open Sans", sans-serif; font-size: 6px; fill: var(--measure-text); }
  .measure-label.key { font-weight: 600; font-size: 7px; }
  .measure-line { stroke: var(--measure); stroke-width: 0.5; fill: none; }
</style>
</head>
<body>
<svg class="binder" viewBox="0 0 1200 637" xmlns="http://www.w3.org/2000/svg">
  <defs>
    <clipPath id="back-cover-clip"><rect x="0" y="0" width="549" height="455"/></clipPath>
    <clipPath id="front-cover-clip"><rect x="651" y="0" width="549" height="637"/></clipPath>
  </defs>

  <!-- back cover -->
  <g class="back-cover">
    <rect x="0" y="0" width="549" height="455" fill="var(--navy)"/>
    <rect x="0" y="455" width="549" height="8" fill="var(--gold)"/>
    <rect x="0" y="463" width="549" height="174" fill="var(--paper)"/>
    <g clip-path="url(#back-cover-clip)">
      <circle cx="287" cy="255" r="137" fill="none" stroke="var(--navy-ring)" stroke-width="6"/>
      <circle cx="287" cy="255" r="121" fill="var(--navy-deep)" role="img" aria-label="Große, dezente Markenfläche im Hintergrund"/>
    </g>
    <g class="punch-holes" fill="var(--hole)">
      <circle cx="511" cy="241" r="6.5"/>
      <circle cx="452" cy="269" r="6.5"/>
      <circle cx="452" cy="368" r="6.5"/>
      <circle cx="511" cy="396" r="6.5"/>
    </g>
    <g class="back-brand">
      <circle cx="101" cy="503" r="25" fill="var(--navy)" stroke="var(--gold)" stroke-width="2"/>
      <text class="brand-name" x="136" y="506" font-size="17" fill="var(--navy)">Tierpraxoland</text>
      <text class="brand-tag" x="136" y="516" font-size="8" fill="var(--gold)">Fachklinik für Kleintiere</text>
    </g>
    <g class="contact">
      <text class="strong" x="75" y="549">Tierpraxoland GmbH &amp; Co KG</text>
      <text class="strong" x="75" y="559">Lindenweg 48, 1140 Wien</text>
      <text class="soft" x="75" y="569">Handelsgericht Wien, FN 412093kt</text>
      <text class="soft" x="75" y="579">GF: Dr. Lena Berger, ATU 5213408</text>
      <line x1="237" y1="542" x2="237" y2="580" stroke="#c8cbcf" stroke-width="1"/>
      <text class="soft" x="260" y="549">+43 (1) 480 5510</text>
      <text class="soft" x="260" y="559">+43 (1) 480 5511</text>
      <text class="soft" x="260" y="569">info@tierpraxoland.at</text>
      <text class="soft" x="260" y="579">www.tierpraxoland.at</text>
    </g>
  </g>

  <!-- spine -->
  <g class="spine">
    <rect x="549" y="0" width="102" height="637" fill="var(--gold)"/>
    <circle cx="600" cy="456" r="25" fill="var(--label-grey)" stroke="var(--trim)" stroke-width="4"/>
    <circle cx="600" cy="547" r="41" fill="#ffffff" fill-opacity="0.12" stroke="#ffffff" stroke-opacity="0.18" stroke-width="2"/>
  </g>

  <!-- front cover -->
  <g class="front-cover">
    <rect x="651" y="0" width="549" height="637" fill="var(--navy)"/>
    <g clip-path="url(#front-cover-clip)">
      <circle cx="1062" cy="548" r="150" fill="none" stroke="var(--navy-ring)" stroke-width="7"/>
      <circle cx="1062" cy="548" r="131" fill="var(--navy-deep)" role="img" aria-label="Große, dezente Markenfläche im Hintergrund"/>
    </g>
    <circle cx="912" cy="192" r="66" fill="var(--white)" stroke="var(--gold)" stroke-width="4"/>
    <text class="brand-name" x="912" y="306" font-size="40" fill="var(--white)" text-anchor="middle">Tierpraxoland</text>
    <text class="brand-tag" x="912" y="335" font-size="21" fill="var(--gold)" text-anchor="middle">Fachklinik für Kleintiere</text>
  </g>

  <!-- print guides -->
  <g class="guides">
    <rect x="28" y="28" width="1143" height="581" fill="none" stroke="var(--trim)" stroke-width="0.8"/>
    <g stroke="#3b6d9a" stroke-width="0.4" stroke-dasharray="2 2">
      <line x1="541" y1="28" x2="541" y2="609"/>
      <line x1="556" y1="28" x2="556" y2="609"/>
      <line x1="644" y1="28" x2="644" y2="609"/>
    </g>
    <g stroke="#e8c24a" stroke-width="0.5" stroke-dasharray="2 2">
      <line x1="549" y1="28" x2="549" y2="609"/>
      <line x1="651" y1="28" x2="651" y2="609"/>
    </g>
  </g>

  <!-- measurements -->
  <g class="measurements">
    <line class="measure-line" x1="28" y1="115" x2="1171" y2="115"/>
    <text class="measure-label key" x="600" y="113" text-anchor="middle">62,0 cm</text>

    <line class="measure-line" x1="0" y1="414" x2="1200" y2="414"/>
    <text class="measure-label" x="14" y="412" text-anchor="middle">1,5 cm</text>
    <text class="measure-label" x="288" y="412" text-anchor="middle">28,2 cm</text>
    <text class="measure-label" x="600" y="412" text-anchor="middle">5,6 cm</text>
    <text class="measure-label" x="912" y="412" text-anchor="middle">28,2 cm</text>
    <text class="measure-label" x="1186" y="412" text-anchor="middle">1,5 cm</text>

    <line class="measure-line" x1="152" y1="0" x2="152" y2="637"/>
    <text class="measure-label" transform="translate(150 14) rotate(-90)" text-anchor="middle">1,5 cm</text>
    <text class="measure-label key" transform="translate(150 319) rotate(-90)" text-anchor="middle">31,5 cm</text>
    <text class="measure-label" transform="translate(150 623) rotate(-90)" text-anchor="middle">1,5 cm</text>

    <line class="measure-line" x1="509" y1="181" x2="549" y2="181"/>
    <text class="measure-label" x="525" y="179" text-anchor="middle">4 mm</text>
    <line class="measure-line" x1="651" y1="181" x2="691" y2="181"/>
    <text class="measure-label" x="674" y="179" text-anchor="middle">4 mm</text>
    <line class="measure-line" x1="549" y1="201" x2="587" y2="201"/>
    <text class="measure-label" x="571" y="199" text-anchor="middle">4 mm</text>
    <line class="measure-line" x1="613" y1="201" x2="651" y2="201"/>
    <text class="measure-label" x="628" y="199" text-anchor="middle">4 mm</text>

    <line class="measure-line" x1="600" y1="484" x2="600" y2="609"/>
    <text class="measure-label" transform="translate(598 545) rotate(-90)" text-anchor="middle">7,0 cm</text>
  </g>
</svg>
</body>
</html>
```